Modern Podcast Marketing Cards - BRAVOKESTRAL

Update: Do "not" include my address, there's no need for this. Please remember this project needs to promote my brand along with the my new Podcast shows tagline. So this is not a traditional business card, it has to look cool enough so people want to hold onto it and not just toss it aside. So obviously "not" an old school boring business card with a ton of business contact info/text. Needs to catch attention and drive my recipients to want to visit the website " bravokestral.net " and/or to download and listen on the apps Tunevale, Weavly, Mondro Spin. Plus would like to drive them to Follow on my social media channels @BRAVOKESTRAL; all while making sure the the design doesn't look cluttered while not being boring.
I've re-designed the logo specifically for the new show though vs what you see when you first visit my website. So the shows logo is also attached which is found on Tunevale, Weavly app, etc. That design is to promote the three domains this brand focused on "Fueling" the followers and listeners with, regarding "Health", "Business", and "Lifestyle". If logos end up on both sides of the card, one should have the version with the three words included of Health, Business, and Lifestyle. The other side should use the blank version of the logo attached which does not have those three words under the BRAVOKESTRAL logo. So I gave you two versions to work with.
**Try and work in my three domains mentioned above and/or the actual tagline for the show/my brand which is "SPARK Your Health, Business, and Lifestyle". You can break it up a little if it will stand out stronger. Remember this is more of a marketing/advertising card vs a boring traditional business card.
Just to note, my profession behind the Podcast Host is my consulting as a Sales, Marketing, and Business Development consultant, But the final design should really show off my Tagline and those three domains to "SPARK Your Health, Business, and Lifestyle!" (without being cluttered)
- again I like it when the flames get ghosted or used as a transparent backdrop. Or you can somehow take a podcast microphone and overlay my logo's flames to wrap around the microphone or have the microphone stand out with "fire fueling it".
Why the three domains focus?
1. Health: because I'm a health nut, adrenaline junkie sports participant, GritLoop coach, and I have a part time nutritional business.
2. Business: because I'm a business consultant specializing in online branding and social media marketing, with 20 years of business experience.
3. Lifestyle: because I do a lot of coaching on life balance, motivational speaking, love to travel, and am always promoting people to balance their lifestyle between business, personal, and fun.

Target Market(s)

Podcasting, Online Branding & Marketing

Industry/Entity Type

Marketing

Contact Information for Business Card

More of a marketing card than a traditional business card, Double-sided, rich bold colors used from my logo's colors. Will consider the clear plastic style too.

Font styles to use
Serif
Sans Serif

Requirements
Must have
• - Drive people to want to visit the website and download/listen to my podcast via the three apps.
• - So use those apps logos somehow from Tunevale Podcast app, Weavly Radio app, and the Mondro Spin app logos.
• - For contact info: My Name, Titles are Chief Intrepid Officer, also include Podcaster for the 2nd title. Contact info should be 1st my email, 2nd my website address without the www; and third my phone.
• Note: reduce clutter and make sure it's not too busy. That's why I'm considering a 2 sided design.
Nice to have
• - Colors should coincide with my logo and primary colors from the logos.
• - Not too much white, at least side should be a gray or blue backdrop
• - I love the style where you take the flames from my logo and ghost or make them transparent on the backdrop for the background on the card.
• - A podcast microphone logo included somehow or set it one fire with my fire from my logo would be cool.
Should not have
• - Do not list my address
• - No single sided cards
• - No crazy stripes or swoosh marks, emphasis is the FIRE so motivate people, and inspire, "to fire them up" with your design.

```html
<!DOCTYPE html>
<html lang="en">
<head>
<meta charset="utf-8">
<title>BRAVOKESTRAL – Podcast Marketing Cards</title>
<link rel="stylesheet" href="https://fonts.googleapis.com/css2?family=Open+Sans:wght@400;600;700&family=Oswald:wght@400;600&display=swap">
<style>
  :root {
    --stage: #e8e5df;
    --card-white: #ffffff;
    --card-grey: #eeeeee;
    --brand-blue: #24338a;
    --brand-blue-deep: #17215e;
    --brand-blue-light: #33489f;
    --ink-black: #0b0b0b;
    --text-dark: #1d1d1d;
    --ring-grey: #c9c9c9;
    --rule-grey: #9a9a9a;
    --ghost-blue: rgba(80, 110, 200, 0.22);
    --text-light: #ffffff;
    --text-soft: rgba(255, 255, 255, 0.85);
  }
  * { box-sizing: border-box; margin: 0; padding: 0; }
  html, body { width: 1200px; height: 780px; overflow: hidden; }
  body {
    background: var(--stage);
    font-family: "Open Sans", Arial, sans-serif;
    position: relative;
  }
  .card {
    position: absolute;
    top: 235px;
    width: 540px;
    height: 310px;
    border-radius: 4px;
    overflow: hidden;
    box-shadow: 0 10px 24px rgba(0, 0, 0, 0.18);
  }

  /* Front side */
  .card-front {
    left: 40px;
    background: linear-gradient(160deg, var(--card-white), var(--card-grey));
  }
  .band { position: absolute; }
  .band-black-thin { left: 262px; right: 0; top: 8px; height: 7px; background: var(--ink-black); }
  .band-black { left: 262px; right: 0; top: 24px; height: 82px; background: var(--ink-black); }
  .band-blue-thin { left: 0; width: 150px; top: 8px; height: 7px; background: var(--brand-blue); }
  .band-blue { left: 0; width: 150px; top: 24px; height: 82px; background: var(--brand-blue); }
  .band-blue-edge { left: 0; width: 150px; top: 112px; height: 4px; background: var(--brand-blue); }

  .brand-badge {
    position: absolute;
    left: 146px;
    top: 6px;
    width: 120px;
    height: 120px;
    border-radius: 50%;
    background: var(--card-white);
    border: 2px solid var(--ring-grey);
    display: flex;
    align-items: center;
    justify-content: center;
  }
  .brand-badge-name {
    font-family: "Oswald", "Arial Narrow", sans-serif;
    font-weight: 600;
    font-size: 16px;
    letter-spacing: 0.5px;
    color: var(--brand-blue);
  }

  .tagline {
    position: absolute;
    left: 40px;
    top: 150px;
    font-size: 15px;
    color: var(--text-dark);
  }
  .identity {
    position: absolute;
    left: 40px;
    top: 194px;
    width: 210px;
  }
  .person-name {
    font-weight: 600;
    font-size: 21px;
    color: var(--brand-blue);
    line-height: 1.1;
  }
  .person-title {
    font-size: 14px;
    line-height: 20px;
    color: var(--text-dark);
  }
  .person-title:first-of-type { margin-top: 4px; }
  .divider {
    position: absolute;
    left: 262px;
    top: 190px;
    width: 1px;
    height: 96px;
    background: var(--rule-grey);
  }
  .contact-list {
    position: absolute;
    left: 278px;
    top: 188px;
    list-style: none;
    font-size: 14px;
    line-height: 24px;
    color: var(--text-dark);
  }
  .contact-label {
    display: inline-block;
    width: 18px;
    color: var(--brand-blue);
    font-weight: 600;
  }

  /* Back side */
  .card-back {
    left: 620px;
    background: radial-gradient(ellipse at 45% 45%, var(--brand-blue-light), var(--brand-blue) 55%, var(--brand-blue-deep));
  }
  .ghost-flames {
    position: absolute;
    left: 40px;
    top: 20px;
    width: 300px;
    height: 270px;
    border-radius: 50%;
    background: radial-gradient(ellipse at center, var(--ghost-blue), rgba(80, 110, 200, 0) 70%);
  }
  .back-content {
    position: absolute;
    right: 38px;
    top: 52px;
    text-align: right;
    color: var(--text-light);
  }
  .wordmark {
    font-family: "Oswald", "Arial Narrow", sans-serif;
    font-weight: 600;
    font-size: 62px;
    line-height: 1;
    letter-spacing: 1px;
  }
  .domains {
    font-family: "Oswald", "Arial Narrow", sans-serif;
    font-weight: 400;
    font-size: 19px;
    letter-spacing: 4px;
    margin-top: 10px;
  }
  .profession {
    font-size: 13px;
    margin-top: 24px;
    color: var(--text-soft);
  }
  .listen-row {
    position: absolute;
    right: 38px;
    bottom: 28px;
    display: flex;
    align-items: center;
    gap: 16px;
    font-size: 13px;
    color: var(--text-light);
  }
  .listen-label { font-weight: 600; }
  .app-name { display: flex; align-items: center; gap: 6px; }
  .app-dot {
    width: 10px;
    height: 10px;
    border-radius: 50%;
    background: var(--text-light);
  }
</style>
</head>
<body>

<section class="card card-front" aria-label="Card front">
  <div class="band band-blue-thin"></div>
  <div class="band band-blue"></div>
  <div class="band band-blue-edge"></div>
  <div class="band band-black-thin"></div>
  <div class="band band-black"></div>

  <div class="brand-badge"><span class="brand-badge-name">BRAVOKESTRAL</span></div>

  <p class="tagline">SPARK Your Health, Business, and Lifestyle!</p>

  <div class="identity">
    <p class="person-name">DANE CORWELL</p>
    <p class="person-title">Chief Intrepid Officer</p>
    <p class="person-title">Podcaster</p>
  </div>

  <div class="divider"></div>

  <ul class="contact-list">
    <li><span class="contact-label">E:</span>dane@bravokestral.net</li>
    <li><span class="contact-label">W:</span>bravokestral.net</li>
    <li><span class="contact-label">P:</span>+1 555-014-2278</li>
    <li><span class="contact-label">@</span>BRAVOKESTRAL</li>
  </ul>
</section>

<section class="card card-back" aria-label="Card back">
  <div class="ghost-flames" role="img" aria-label="Ghosted flame artwork in faint blue behind the brand name"></div>
  <div class="back-content">
    <p class="wordmark">BRAVOKESTRAL</p>
    <p class="domains">HEALTH | BUSINESS | LIFESTYLE</p>
    <p class="profession">Sales, Marketing, and Business Development consultant</p>
  </div>
  <div class="listen-row">
    <span class="listen-label">Listen on</span>
    <span class="app-name"><span class="app-dot"></span>Tunevale</span>
    <span class="app-name"><span class="app-dot"></span>Weavly</span>
    <span class="app-name"><span class="app-dot"></span>Mondro Spin</span>
  </div>
</section>

</body>
</html>
```